Harbourline capital partners pty ltd

Hi guys I recently opened a brokerage company. I need a flyer to capture the attention of customers.
I would like something professional and cool at the same time.
My website is harbourcp-example.com.au
I also attached the current flyer. as you can see it lacks of originality and it isn't cool!!!!
Thank you

Target Market(s)

People between the age of 18-50

Industry/Entity Type

Financial Service

Requirements
Must have
• Mast have features and contents that reflects the website
• harbourcp-example.com.au
Nice to have
• Open to anything
Should not have
• Not to sure

```html
<!DOCTYPE html>
<html lang="en">
<head>
<meta charset="utf-8">
<title>Harbourline Capital Partners – Financing Flyer</title>
<link rel="stylesheet" href="https://fonts.googleapis.com/css2?family=Montserrat:wght@500;600;700&family=Open+Sans:wght@400;600&display=swap">
<style>
:root{
  --blue:#1f9ad9;
  --blue-dark:#1485c7;
  --blue-light:#4db5ea;
  --orange:#f7941d;
  --orange-dark:#ef7d12;
  --ink:#1a1a1a;
  --white:#ffffff;
  --panel-edge:#f39a2b;
}
*{box-sizing:border-box;margin:0;padding:0}
html,body{width:902px;height:1200px;overflow:hidden;background:#fff}
.flyer{position:relative;width:902px;height:1200px;background:var(--white);font-family:"Open Sans",Arial,sans-serif;color:var(--ink);overflow:hidden}

/* header */
.brand{position:absolute;left:34px;top:48px;display:flex;align-items:center;gap:12px}
.brand-dot{width:34px;height:34px;border-radius:50%;background:var(--blue)}
.brand-name{font-family:"Open Sans",Arial,sans-serif;font-weight:600;color:var(--blue);font-size:19px;line-height:1.2;text-transform:uppercase;letter-spacing:.3px}
.headline{position:absolute;right:24px;top:18px;text-align:right;font-family:"Montserrat",Arial,sans-serif;font-weight:700;line-height:1.18}
.headline-top{color:var(--blue);font-size:39px}
.headline-bottom{color:var(--orange);font-size:38px;letter-spacing:.5px}

/* hero */
.hero-photo{position:absolute;left:0;top:139px;width:639px;height:404px;background:linear-gradient(120deg,#e9eef2 0%,#f4f5f6 45%,#cfdbe6 100%)}
.hero-banner{position:absolute;top:459px;height:84px;display:flex;align-items:center;font-family:"Montserrat",Arial,sans-serif;font-weight:700;color:var(--white);font-size:31px;letter-spacing:1px;white-space:nowrap}
.hero-banner--blue{left:0;width:286px;background:rgba(31,154,217,.82);justify-content:center}
.hero-banner--orange{left:292px;width:347px;background:rgba(247,148,29,.85);padding-left:66px;border-bottom-right-radius:40px}

.why{position:absolute;left:655px;top:139px;width:226px;height:404px;background:linear-gradient(180deg,var(--blue-light),var(--blue-dark));border-bottom-left-radius:70px;padding:12px 14px 0 0;text-align:right;color:var(--white)}
.why-title{font-family:"Montserrat",Arial,sans-serif;font-weight:600;font-size:24px;letter-spacing:.5px;margin-bottom:8px}
.why-list{list-style:none}
.why-list li{position:relative;padding-right:22px;font-size:16.5px;line-height:23px;margin-bottom:9px}
.why-list li::after{content:"";position:absolute;right:0;top:6px;width:11px;height:11px;border-radius:50%;background:var(--orange);border:1.5px solid var(--white)}

/* info panel */
.info{position:absolute;left:21px;top:556px;width:858px;height:295px;border:2px solid var(--panel-edge);border-radius:18px;background:linear-gradient(180deg,#fff,#f5f5f5);padding:6px 20px 0 18px}
.section-title{display:flex;align-items:center;gap:8px;font-family:"Montserrat",Arial,sans-serif;font-weight:700;color:var(--blue);font-size:19px;letter-spacing:.5px}
.section-icon{width:28px;height:28px;border-radius:50%;border:2px solid var(--orange)}
.section-text{font-size:13.3px;line-height:17.5px;margin:3px 0 0 0;text-align:justify}
.section-title--second{margin-top:14px}
.lenders{position:relative;height:100px;margin-top:6px}
.lender-col{position:absolute;top:0;list-style:none}
.lender-col li{position:relative;padding-left:20px;font-size:12.5px;height:25px;line-height:18px;white-space:nowrap}
.lender-col li::before{content:"";position:absolute;left:0;top:3px;width:11px;height:11px;border:1.5px solid var(--orange)}
.lender-col li::after{content:"";position:absolute;left:3px;top:2px;width:5px;height:9px;border-right:2px solid var(--orange-dark);border-bottom:2px solid var(--orange-dark);transform:rotate(40deg)}
.lender-col--1{left:6px}
.lender-col--2{left:177px}
.lender-col--3{left:391px}
.lender-col--4{left:536px}
.lender-col--5{left:702px}

/* specialise */
.specialise-pill{position:absolute;left:237px;top:862px;width:429px;height:36px;border-radius:18px;background:var(--orange);color:var(--white);font-family:"Montserrat",Arial,sans-serif;font-weight:600;font-size:20px;text-align:center;line-height:36px;letter-spacing:.5px;box-shadow:0 6px 8px -6px rgba(0,0,0,.35)}
.asset{position:absolute;display:flex;align-items:center;gap:20px}
.asset-icon{width:96px;height:92px}
.asset-label{font-family:"Montserrat",Arial,sans-serif;font-weight:600;font-size:17px;letter-spacing:.5px;line-height:1.3}

/* footer */
.footer-rule{position:absolute;left:0;top:1147px;width:902px;height:2px;background:var(--orange)}
.footer{position:absolute;left:0;top:1153px;width:902px;height:47px;background:var(--blue);color:var(--white);font-size:11.5px}
.contact{position:absolute;top:0;height:47px;display:flex;align-items:center;gap:6px;white-space:nowrap}
.contact svg{width:12px;height:12px;flex:none}
</style>
</head>
<body>
<div class="flyer">

  <header>
    <div class="brand">
      <span class="brand-dot"></span>
      <span class="brand-name">Harbourline Capital<br>Partners Pty Ltd</span>
    </div>
    <h1 class="headline">
      <span class="headline-top">We specialize in</span><br>
      <span class="headline-bottom">FINANCING!</span>
    </h1>
  </header>

  <div class="hero-photo" role="img" aria-label="Photo of a young couple reviewing loan papers with a finance broker at a desk"></div>
  <div class="hero-banner hero-banner--blue">HARBOURLINE</div>
  <div class="hero-banner hero-banner--orange">CAPITAL</div>

  <aside class="why">
    <h2 class="why-title">WHY USE US</h2>
    <ul class="why-list">
      <li>Low Rates</li>
      <li>Access Australia’s<br>most trusted lenders</li>
      <li>Quick &amp; easy,<br>same day approvals</li>
      <li>Professional Advice<br>New, Used, private<br>or dealer sale -<br>the choice is yours</li>
      <li>100% Finance<br>available</li>
      <li>BAD credit finance</li>
    </ul>
  </aside>

  <section class="info">
    <h3 class="section-title"><span class="section-icon"></span>WE ARE</h3>
    <p class="section-text">Harbourline capital partners is a bespoke brokerage firm established by a team of professionals who bring with them over 50 year’s combined experience in consulting, finance, negotiation, and executive roles within the finance and automotive industry. We strive for excellence, delivering the right solution for our clients in a timely and professional manner.</p>
    <h3 class="section-title section-title--second"><span class="section-icon"></span>OUR FINANCIERS INCLUDE</h3>
    <p class="section-text">We have privileged and specialized access to a wide range of lenders enabling us to tailor solutions which cater to your individual needs.</p>
    <div class="lenders">
      <ul class="lender-col lender-col--1">
        <li>Marlow Finance</li><li>Ridgeway Leasing</li><li>Autovia Finance</li><li>Keelwater Finance</li>
      </ul>
      <ul class="lender-col lender-col--2">
        <li>Saltbush Asset finance</li><li>Motorra Finance</li><li>Crest and Common Finance</li><li>Rivolt Finance</li>
      </ul>
      <ul class="lender-col lender-col--3">
        <li>Tidal Finance</li><li>EASTMARK</li><li>OPAL</li><li>KIRA</li>
      </ul>
      <ul class="lender-col lender-col--4">
        <li>NEXA FINANCE</li><li>ARO</li><li>Bank Of Lakeside</li><li>Bank Ridge</li>
      </ul>
      <ul class="lender-col lender-col--5">
        <li>Sunridge Bank</li><li>Altura</li><li>Coastal Bank</li><li>Farther Bank</li>
      </ul>
    </div>
  </section>

  <h2 class="specialise-pill">WE SPECIALISE IN FINANCING</h2>

  <svg width="0" height="0" style="position:absolute">
    <defs>
      <radialGradient id="icon-fill" cx="40%" cy="35%" r="70%">
        <stop offset="0" stop-color="#5cc0f0"/>
        <stop offset="1" stop-color="#1487ca"/>
      </radialGradient>
    </defs>
  </svg>

  <div class="asset" style="left:45px;top:915px">
    <svg class="asset-icon" viewBox="0 0 96 92"><ellipse cx="48" cy="46" rx="47" ry="45" fill="url(#icon-fill)"/>
      <path d="M22 58 V48 Q24 40 32 38 L44 32 H62 Q70 34 72 46 V58 Z" fill="#fff"/>
      <circle cx="33" cy="59" r="6" fill="#fff" stroke="#1a8fd0" stroke-width="2"/><circle cx="63" cy="59" r="6" fill="#fff" stroke="#1a8fd0" stroke-width="2"/>
      <path d="M47 36 H60 Q65 38 66 45 H47 Z" fill="#1a8fd0"/></svg>
    <span class="asset-label">CARS</span>
  </div>

  <div class="asset" style="left:328px;top:915px">
    <svg class="asset-icon" viewBox="0 0 96 92"><ellipse cx="48" cy="46" rx="47" ry="45" fill="url(#icon-fill)"/>
      <rect x="42" y="22" width="10" height="10" fill="#fff"/><rect x="34" y="32" width="28" height="10" fill="#fff"/>
      <path d="M24 44 H72 L66 58 H30 Z" fill="#fff"/>
      <path d="M22 64 q6 -4 12 0 t12 0 t12 0 t12 0 t6 0" fill="none" stroke="#fff" stroke-width="3"/></svg>
    <span class="asset-label">BOATS</span>
  </div>

  <div class="asset" style="left:610px;top:915px">
    <svg class="asset-icon" viewBox="0 0 96 92"><ellipse cx="48" cy="46" rx="47" ry="45" fill="url(#icon-fill)"/>
      <path d="M18 56 V40 Q20 30 34 30 H66 Q72 30 72 40 V56 Z" fill="#fff"/>
      <rect x="28" y="38" width="14" height="9" fill="#1a8fd0"/><rect x="52" y="38" width="10" height="16" fill="#1a8fd0"/>
      <path d="M72 52 H82" stroke="#fff" stroke-width="3"/><circle cx="42" cy="58" r="5" fill="#fff" stroke="#1a8fd0" stroke-width="2"/></svg>
    <span class="asset-label">CARAVANS</span>
  </div>

  <div class="asset" style="left:45px;top:1022px">
    <svg class="asset-icon" viewBox="0 0 96 92"><ellipse cx="48" cy="46" rx="47" ry="45" fill="url(#icon-fill)"/>
      <path d="M20 56 L26 46 H46 L52 38 H60 L64 46 H74 Q76 52 70 56 Z" fill="#fff"/>
      <path d="M20 64 q6 -4 12 0 t12 0 t12 0 t12 0 t6 0" fill="none" stroke="#fff" stroke-width="3"/></svg>
    <span class="asset-label">JET SKIS</span>
  </div>

  <div class="asset" style="left:328px;top:1022px">
    <svg class="asset-icon" viewBox="0 0 96 92"><ellipse cx="48" cy="46" rx="47" ry="45" fill="url(#icon-fill)"/>
      <rect x="32" y="18" width="32" height="8" fill="#fff"/><rect x="30" y="28" width="36" height="30" rx="3" fill="#fff"/>
      <rect x="35" y="32" width="26" height="10" fill="#1a8fd0"/>
      <rect x="33" y="60" width="8" height="10" fill="#fff"/><rect x="55" y="60" width="8" height="10" fill="#fff"/></svg>
    <span class="asset-label">TRUCKS</span>
  </div>

  <div class="asset" style="left:610px;top:1022px">
    <svg class="asset-icon" viewBox="0 0 96 92"><ellipse cx="48" cy="46" rx="47" ry="45" fill="url(#icon-fill)"/>
      <rect x="20" y="44" width="30" height="12" fill="#fff"/><rect x="32" y="34" width="14" height="12" fill="#fff"/>
      <path d="M50 46 L62 30 L74 44 L68 52" fill="none" stroke="#fff" stroke-width="4"/>
      <path d="M64 52 L76 50 L72 60 Z" fill="#fff"/>
      <circle cx="26" cy="60" r="5" fill="#fff"/><circle cx="44" cy="60" r="5" fill="#fff"/></svg>
    <span class="asset-label">EARTH MOVING<br>EQUIPMENTS</span>
  </div>

  <div class="footer-rule"></div>
  <footer class="footer">
    <span class="contact" style="left:28px">
      <svg viewBox="0 0 12 12"><path d="M6 0 a4 4 0 0 1 4 4 c0 3 -4 8 -4 8 s-4 -5 -4 -8 a4 4 0 0 1 4 -4z" fill="#fff"/><circle cx="6" cy="4" r="1.5" fill="#1f9ad9"/></svg>
      14 Wharf Lane, Kingsford ACT 2600
    </span>
    <span class="contact" style="left:292px">
      <svg viewBox="0 0 12 12"><path d="M2 1 L4 1 L5 4 L3.5 5 Q5 7.5 7 8.5 L8 7 L11 8 L11 10 Q10 11.5 8 11 Q2 9 1 3 Q1 1.5 2 1z" fill="#fff"/></svg>
      +61 400 555 018
    </span>
    <span class="contact" style="left:440px">
      <svg viewBox="0 0 12 12"><rect x="0.5" y="2" width="11" height="8" fill="#fff"/><path d="M0.5 2 L6 6.5 L11.5 2" fill="none" stroke="#1f9ad9" stroke-width="1"/></svg>
      admin@harbourcp-example.com.au
    </span>
    <span class="contact" style="left:684px">
      <svg viewBox="0 0 12 12"><circle cx="6" cy="6" r="5.5" fill="#fff"/><path d="M1 6 H11 M6 0.5 Q3 6 6 11.5 M6 0.5 Q9 6 6 11.5" fill="none" stroke="#1f9ad9" stroke-width="0.8"/></svg>
      www.harbourcp-example.com.au
    </span>
  </footer>

</div>
</body>
</html>
```